Career Development Skills | Business Card & Logo Design

We are looking for a business card including logo design for a new Sydney based business called 'Bright Pathway'.
We offer a range of services that focus on building the Employability or Employment skills for individuals focusing on job seekers and those interested in building skills required to develop their career. Employability skills are required not only to gain employment, but also to progress within an organisation so as to achieve one's potential.
Target Market(s)
Our client targets include corporates and govt agencies looking to build skills within their current employee base or assist staff in the transition between roles or workplaces.
Industry/Entity Type
Business
Look and feel
Each slider illustrates characteristics of the customer's brand and the style your logo design should communicate.

```html
<!DOCTYPE html>
<html lang="en">
<head>
<meta charset="UTF-8">
<title>Bright Pathway – Business Card</title>
<link href="https://fonts.googleapis.com/css2?family=Noto+Serif:wght@400;700&display=swap" rel="stylesheet">
<style>
  :root {
    --brand-red: #ec1c24;
    --ink: #1a1a1a;
    --paper: #ffffff;
    --edge: #9a9a9a;
  }
  html, body {
    margin: 0;
    padding: 0;
    overflow: hidden;
  }
  body {
    width: 1200px;
    height: 900px;
    background: var(--paper);
    position: relative;
    font-family: "Noto Serif", Georgia, serif;
  }
  .card {
    position: absolute;
    top: 290px;
    width: 530px;
    height: 320px;
    border-radius: 16px;
    overflow: hidden;
    box-sizing: border-box;
  }
  /* Front */
  .card-front {
    left: 60px;
    background: var(--paper);
    border: 1.5px solid var(--edge);
  }
  .card-front .footer-band {
    position: absolute;
    left: 0;
    right: 0;
    bottom: 0;
    height: 92px;
    background: var(--brand-red);
    display: flex;
    align-items: center;
    justify-content: center;
  }
  .card-front .web {
    color: var(--paper);
    font-size: 27px;
    letter-spacing: 0.3px;
  }
  .brand {
    position: absolute;
    display: flex;
    align-items: center;
  }
  .brand-dot {
    border-radius: 50%;
    background: var(--brand-red);
    flex: none;
  }
  .brand-name {
    font-weight: 700;
    color: var(--ink);
    white-space: nowrap;
  }
  .card-front .brand {
    left: 30px;
    top: 60px;
    gap: 20px;
  }
  .card-front .brand-dot {
    width: 120px;
    height: 120px;
  }
  .card-front .brand-name {
    font-size: 36px;
  }
  /* Back */
  .card-back {
    left: 600px;
    background: var(--brand-red);
    color: var(--paper);
  }
  .card-back .web {
    position: absolute;
    left: 24px;
    top: 52px;
    font-size: 19px;
  }
  .brand-tab {
    position: absolute;
    right: 0;
    top: 30px;
    width: 280px;
    height: 74px;
    background: var(--paper);
    border-radius: 14px 0 0 14px;
  }
  .brand-tab .brand {
    left: 14px;
    top: 13px;
    gap: 12px;
  }
  .brand-tab .brand-dot {
    width: 48px;
    height: 48px;
  }
  .brand-tab .brand-name {
    font-size: 19px;
  }
  .person {
    position: absolute;
    left: 24px;
    top: 210px;
  }
  .person-name {
    font-size: 27px;
    line-height: 1.1;
    margin: 0;
    font-weight: 400;
  }
  .person-role {
    font-size: 17px;
    margin: 6px 0 4px;
  }
  .person-email {
    font-size: 13px;
  }
  .address {
    position: absolute;
    left: 286px;
    top: 176px;
    margin: 0;
    font-style: normal;
    font-size: 16px;
    line-height: 19px;
  }
</style>
</head>
<body>
  <section class="card card-front">
    <div class="brand">
      <span class="brand-dot"></span>
      <span class="brand-name">Bright Pathway</span>
    </div>
    <div class="footer-band">
      <span class="web">brightpathway.com.au</span>
    </div>
  </section>

  <section class="card card-back">
    <span class="web">brightpathway.com.au</span>
    <div class="brand-tab">
      <div class="brand">
        <span class="brand-dot"></span>
        <span class="brand-name">Bright Pathway</span>
      </div>
    </div>
    <div class="person">
      <h1 class="person-name">Daniel Hartley</h1>
      <div class="person-role">Director</div>
      <div class="person-email">daniel@brightpathway.com.au</div>
    </div>
    <address class="address">
      Level 14<br>
      Harbour View Tower 3<br>
      88 Kent Street<br>
      Millers Point, Sydney 2000<br>
      Phone (02) 9555 0142<br>
      Fax (02) 9555 0143
    </address>
  </section>
</body>
</html>
```